Door Hanger Design for Electricians Serving Homes

I would like our logo incorporated into the door hanger. We would like a place for a tear off section on the bottom of the hanger with our contact information: K&T Electric - (555) 318-4702 - www.kandtelectric.example - info@kandtelectric.example.
Door Hanger Script
Front Side of the Door Hanger:
[Company Logo]
Need a Reliable Electrician?
Your Local Electrical Expert is Just Around the Corner!
• Quick Response Times
• Affordable Rates
• Quality Workmanship
• Fully Licensed & Insured
• Special Offer:
• 10% OFF Your First Service Call!
Back Side of the Door Hanger:
Don't Let Electrical Issues Keep You in the Dark!
From flickering lights to complete system upgrades, we've got all your
residential electrical needs covered. Our services include:
• Electrical Repairs & Troubleshooting
• Lighting Installation & Upgrades
• Safety Inspections & Code Compliance
• Energy-Efficient Solutions
• 24/7 Emergency Services
• Why Choose Us?
• Friendly, Local Service
• Over 30 Years of Experience
• Satisfaction Guaranteed
• Upfront Pricing
Call Us Today: [Your Phone Number]
Visit Our Website: [Your Website]
Book Your Appointment Now and Claim Your 10% Discount!
Offer valid for new customers on the first visit only. Mention this door hanger when
booking.
[Your Company Name and Contact Information]
Follow Us on Social Media for More Tips and Special Offers!
[Icons for social media platforms: Chatterpage, Pixmosaic, Quibbler, etc.]
Design Tips:
Use bold, clear fonts for easy reading.
Incorporate your brand colors and logo for instant recognition.
Include a clear call to action (CTA) on both sides.
Add a tear-off section at the bottom with your contact information for
convenience.
Use high-quality images or graphics related to electrical work to catch
the eye.
This door hanger design and copy aim to attract residential clients by
highlighting the benefits of your electrical services, special offers, and
how they can easily get in touch with you for their electrical needs.
The door knocker template will have three of the same design on front and three of the same design on the back. This template is from the print shop.

```html
<!DOCTYPE html>
<html lang="en">
<head>
<meta charset="utf-8">
<title>K&amp;T Electric – Door Hanger</title>
<link rel="stylesheet" href="https://fonts.googleapis.com/css2?family=Bebas+Neue&family=Montserrat:wght@400;500;600;700&display=swap">
<style>
  :root{
    --red:#d71f26;
    --red-dark:#a3141a;
    --ink:#1d1d1d;
    --white:#ffffff;
    --backdrop:#d4a94a;
    --headline:"Bebas Neue", Impact, sans-serif;
    --body:"Montserrat", Arial, sans-serif;
  }
  *{box-sizing:border-box;margin:0;padding:0}
  html,body{width:1200px;height:2918px;overflow:hidden}
  body{background:var(--backdrop);font-family:var(--body);color:var(--ink);position:relative}

  .hanger{position:absolute;left:320px;width:560px;height:1298px;overflow:hidden;background:var(--white);box-shadow:6px 8px 14px rgba(0,0,0,.28)}
  .hanger--front{top:60px}
  .hanger--back{top:1410px;height:1478px;background:var(--red)}

  .photo-top{position:absolute;left:0;top:0;width:560px;height:520px}
  .hanger--front .photo-top{background:linear-gradient(135deg,#3e4450 0%,#6f7785 45%,#9aa0a8 70%,#4a5566 100%)}
  .hanger--back .photo-top{background:linear-gradient(160deg,#c9c3b8 0%,#a89a86 45%,#8a6f52 75%,#b07a5a 100%)}

  .wave{position:absolute;left:0;top:400px;width:560px;height:130px}

  .slit{position:absolute;left:100px;top:0;width:250px;height:6px;background:var(--white);transform-origin:0 50%;transform:rotate(43.9deg)}
  .hole{position:absolute;left:203px;top:96px;width:154px;height:154px;border-radius:50%;background:var(--white)}

  .logo{position:absolute;left:175px;width:210px;height:210px;border-radius:50%;background:var(--white);border:8px solid var(--red);display:flex;align-items:center;justify-content:center}
  .hanger--front .logo{top:311px}
  .hanger--back .logo{top:296px}
  .logo__name{font-family:var(--body);font-weight:700;font-size:25px;color:var(--ink)}

  .headline{position:absolute;left:0;width:560px;text-align:center;font-family:var(--headline);font-weight:400}
  .hanger--front .headline{top:548px;font-size:84px;line-height:78px;color:var(--red)}
  .hanger--back .headline{top:544px;font-size:68px;line-height:57px;color:var(--white)}

  .subhead{position:absolute;left:0;top:714px;width:560px;text-align:center;font-size:25px;line-height:31px;color:var(--ink)}
  .divider{position:absolute;left:144px;top:792px;width:272px;height:3px;background:var(--ink);border:0}

  .checklist{position:absolute;left:46px;list-style:none}
  .checklist li{display:flex;align-items:center;gap:7px;height:33px;font-size:18px}
  .hanger--front .checklist{top:850px}
  .hanger--back .checklist{top:765px}
  .hanger--back .checklist li{height:26.8px;font-size:18.5px;color:var(--white)}
  .tick{width:17px;height:17px;flex:none}

  .bubble{position:absolute;border-radius:50%}
  .bubble--accent{left:367px;top:887px;width:216px;height:216px;background:var(--red)}
  .bubble--team{left:326px;top:831px;width:130px;height:130px;border:4px solid var(--red);background:linear-gradient(150deg,#c7b7a4,#e08a3c 60%,#6b5a4c)}
  .bubble--worker{left:364px;top:892px;width:194px;height:194px;border:4px solid var(--white);background:linear-gradient(150deg,#d8d2ca,#6d6a66 55%,#3a3a3a)}

  .cta-pill{position:absolute;left:125px;top:1130px;width:305px;height:37px;border-radius:19px;background:var(--red);border:2px solid var(--red);display:flex;align-items:center;font-weight:500;font-size:17px}
  .cta-pill__lead{color:var(--white);padding:0 12px 0 16px}
  .cta-pill__offer{flex:1;height:100%;border-radius:17px;background:var(--white);color:var(--red);display:flex;align-items:center;justify-content:center}

  .phone{position:absolute;left:0;width:560px;text-align:center;font-weight:500;font-size:49px;line-height:58px}
  .hanger--front .phone{top:1180px;color:var(--red)}
  .hanger--back .phone{top:1116px;color:var(--white)}

  .web{position:absolute;left:0;width:560px;text-align:center;font-size:22px;line-height:28px;display:flex;justify-content:center;align-items:center;gap:8px}
  .hanger--front .web{top:1242px;color:var(--ink)}
  .hanger--back .web{top:1224px;color:var(--white)}
  .globe{width:18px;height:18px}

  .tag{position:absolute;left:50%;transform:translateX(-50%);height:30px;padding:0 16px;border-radius:15px;background:var(--red-dark);color:var(--white);font-weight:500;font-size:17px;display:flex;align-items:center;white-space:nowrap}
  .tag--call{top:1074px}
  .tag--visit{top:1186px}
  .offer-line{position:absolute;left:0;top:1255px;width:560px;text-align:center;color:var(--white);font-weight:500;font-size:15.5px}

  .terms{position:absolute;left:40px;top:1282px;width:480px;text-align:center;color:var(--white);font-size:12.5px;line-height:16px}
  .social{position:absolute;left:0;top:1322px;width:560px;text-align:center;color:var(--white)}
  .social__lead{font-size:13.5px;font-weight:600;line-height:18px}
  .social__list{list-style:none;display:flex;justify-content:center;gap:22px;margin-top:6px}
  .social__item{display:flex;align-items:center;gap:6px;font-size:13.5px;font-weight:500}
  .social__dot{width:14px;height:14px;border-radius:50%;background:var(--white)}

  .tear-off{position:absolute;left:0;top:1378px;width:560px;height:100px;background:var(--white);border-top:2px dashed var(--ink);display:flex}
  .tear-off__tab{flex:1;display:flex;flex-direction:column;justify-content:center;align-items:center;gap:3px;border-left:1.5px dashed #8a8a8a;text-align:center;padding:0 4px}
  .tear-off__tab:first-child{border-left:0}
  .tear-off__name{font-weight:700;font-size:14px;color:var(--red)}
  .tear-off__line{font-size:10.5px;line-height:13px;color:var(--ink);word-break:break-all}
</style>
</head>
<body>
<svg width="0" height="0" style="position:absolute" aria-hidden="true">
  <symbol id="tick" viewBox="0 0 20 20">
    <circle cx="9" cy="11" r="7" fill="none" stroke="currentColor" stroke-width="2"/>
    <path d="M5.5 10.5 L8.8 14 L18 3" fill="none" stroke="currentColor" stroke-width="2.4" stroke-linecap="round" stroke-linejoin="round"/>
  </symbol>
  <symbol id="globe" viewBox="0 0 20 20">
    <g fill="none" stroke="currentColor" stroke-width="1.6">
      <circle cx="10" cy="10" r="8"/><ellipse cx="10" cy="10" rx="3.5" ry="8"/><path d="M2 10h16M3.5 6h13M3.5 14h13"/>
    </g>
  </symbol>
</svg>

<!-- Front side -->
<section class="hanger hanger--front">
  <div class="photo-top" role="img" aria-label="Photo of an electrician in a hard hat and safety glasses wiring a distribution panel"></div>
  <svg class="wave" viewBox="0 0 560 130" aria-hidden="true">
    <path d="M0 58 Q280 40 560 96 L560 130 L0 130 Z" fill="var(--red)"/>
    <path d="M0 66 Q280 48 560 104 L560 130 L0 130 Z" fill="var(--white)"/>
  </svg>
  <div class="slit"></div>
  <div class="hole"></div>
  <div class="logo"><span class="logo__name">K&amp;T Electric</span></div>

  <h1 class="headline">Need a Reliable<br>Electrician?</h1>
  <p class="subhead">Your Local Electrical Expert<br>is Just Around the Corner!</p>
  <hr class="divider">

  <ul class="checklist" style="color:var(--red)">
    <li><svg class="tick"><use href="#tick"/></svg><span style="color:var(--ink)">Quick Response Times</span></li>
    <li><svg class="tick"><use href="#tick"/></svg><span style="color:var(--ink)">Affordable Rates</span></li>
    <li><svg class="tick"><use href="#tick"/></svg><span style="color:var(--ink)">Quality Workmanship</span></li>
    <li><svg class="tick"><use href="#tick"/></svg><span style="color:var(--ink)">Fully Licensed &amp; Insured</span></li>
    <li><svg class="tick"><use href="#tick"/></svg><span style="color:var(--ink)">Special Offer:</span></li>
    <li><svg class="tick"><use href="#tick"/></svg><span style="color:var(--ink)">10% OFF Your First Service Call!</span></li>
  </ul>

  <div class="bubble bubble--accent"></div>
  <div class="bubble bubble--team" role="img" aria-label="Photo of two electricians in work uniforms"></div>
  <div class="bubble bubble--worker" role="img" aria-label="Photo of an electrician testing an outlet with a multimeter"></div>

  <div class="cta-pill"><span class="cta-pill__lead">CALL NOW A</span><span class="cta-pill__offer">FREE QUOTE</span></div>
  <p class="phone">(555) 318-4702</p>
  <p class="web"><svg class="globe"><use href="#globe"/></svg>www.kandtelectric.example</p>
</section>

<!-- Back side -->
<section class="hanger hanger--back">
  <div class="photo-top" role="img" aria-label="Photo of an electrician with a tool belt carrying a cable reel on a building site"></div>
  <svg class="wave" viewBox="0 0 560 130" aria-hidden="true">
    <path d="M0 62 Q280 10 560 50 L560 130 L0 130 Z" fill="var(--red-dark)"/>
    <path d="M0 70 Q280 18 560 58 L560 130 L0 130 Z" fill="var(--red)"/>
  </svg>
  <div class="slit"></div>
  <div class="hole"></div>
  <div class="logo"><span class="logo__name">K&amp;T Electric</span></div>

  <h2 class="headline">Don't Let Electrical<br>Issues Keep You<br>in the Dark!</h2>

  <ul class="checklist">
    <li><svg class="tick"><use href="#tick"/></svg>Electrical Repairs &amp; Troubleshooting</li>
    <li><svg class="tick"><use href="#tick"/></svg>Lighting Installation &amp; Upgrades</li>
    <li><svg class="tick"><use href="#tick"/></svg>Safety Inspections &amp; Code Compliance</li>
    <li><svg class="tick"><use href="#tick"/></svg>Energy-Efficient Solutions</li>
    <li><svg class="tick"><use href="#tick"/></svg>24/7 Emergency Services</li>
    <li><svg class="tick"><use href="#tick"/></svg>Why Choose Us?</li>
    <li><svg class="tick"><use href="#tick"/></svg>Friendly, Local Service</li>
    <li><svg class="tick"><use href="#tick"/></svg>Over 30 Years of Experience</li>
    <li><svg class="tick"><use href="#tick"/></svg>Satisfaction Guaranteed</li>
    <li><svg class="tick"><use href="#tick"/></svg>Upfront Pricing</li>
  </ul>

  <div class="tag tag--call">CALL NOW TODAY!</div>
  <p class="phone">(555) 318-4702</p>
  <div class="tag tag--visit">VISIT OUR WEBSITE</div>
  <p class="web">www.kandtelectric.example</p>
  <p class="offer-line">Book Your Appointment Now and Claim Your 10% Discount!</p>
  <p class="terms">Offer valid for new customers on the first visit only.<br>Mention this door hanger when booking.</p>

  <div class="social">
    <p class="social__lead">Follow Us on Social Media for More Tips and Special Offers!</p>
    <ul class="social__list">
      <li class="social__item"><span class="social__dot"></span>Chatterpage</li>
      <li class="social__item"><span class="social__dot"></span>Pixmosaic</li>
      <li class="social__item"><span class="social__dot"></span>Quibbler</li>
    </ul>
  </div>

  <div class="tear-off">
    <div class="tear-off__tab"><span class="tear-off__name">K&amp;T Electric</span><span class="tear-off__line">(555) 318-4702</span><span class="tear-off__line">info@kandtelectric.example</span></div>
    <div class="tear-off__tab"><span class="tear-off__name">K&amp;T Electric</span><span class="tear-off__line">(555) 318-4702</span><span class="tear-off__line">info@kandtelectric.example</span></div>
    <div class="tear-off__tab"><span class="tear-off__name">K&amp;T Electric</span><span class="tear-off__line">(555) 318-4702</span><span class="tear-off__line">www.kandtelectric.example</span></div>
    <div class="tear-off__tab"><span class="tear-off__name">K&amp;T Electric</span><span class="tear-off__line">(555) 318-4702</span><span class="tear-off__line">www.kandtelectric.example</span></div>
  </div>
</section>
</body>
</html>
```